Birchline Septic Solutions

Would like to see some single sided ones but would also like to see some double sided with one sided only being the logo. Owners name is Tom Halvick. Phone number is 555-214-0387
Services are pumping, inspections, installs, and repairs

Contact Information for Business Card

555-241-0387 Tom Halvick Maple Ridge, OH

```html
<!DOCTYPE html>
<html lang="en">
<head>
<meta charset="utf-8">
<title>Birchline Septic Solutions – Business Card</title>
<link href="https://fonts.googleapis.com/css2?family=Lato:wght@400;900&display=swap" rel="stylesheet">
<style>
  :root {
    --bg: #2a2a2a;
    --ink: #0d0d0d;
    --paper: #ffffff;
    --teal: #2dbdb8;
    --muted: #2b2b2b;
    --pattern-a: #f1f1f1;
    --pattern-b: #e4e4e4;
  }
  * { box-sizing: border-box; margin: 0; padding: 0; }
  html, body { width: 1200px; height: 875px; overflow: hidden; }
  body {
    background: var(--bg);
    font-family: "Lato", sans-serif;
    position: relative;
  }
  .card {
    position: absolute;
    top: 283px;
    width: 540px;
    height: 309px;
    border-radius: 16px;
    overflow: hidden;
  }
  /* Front: logo side */
  .card-front {
    left: 45px;
    background: var(--ink);
    display: flex;
    align-items: center;
    justify-content: center;
  }
  .brand-front {
    color: var(--paper);
    font-weight: 900;
    font-size: 34px;
    letter-spacing: 2px;
    text-transform: uppercase;
    text-align: center;
    line-height: 1.15;
  }
  /* Back: contact side */
  .card-back {
    left: 615px;
    background: var(--paper);
  }
  .pipe-pattern {
    position: absolute;
    left: 0; top: 60px;
    width: 300px; height: 200px;
    background: radial-gradient(ellipse at 40% 50%, var(--pattern-b), var(--pattern-a) 55%, var(--paper) 80%);
    opacity: .8;
  }
  .brand-back {
    position: absolute;
    right: 28px; top: 30px;
    color: var(--ink);
    font-weight: 900;
    font-size: 17px;
    letter-spacing: 1px;
    text-transform: uppercase;
  }
  .divider-long {
    position: absolute;
    left: 262px; right: 28px; top: 75px;
    height: 1.5px;
    background: var(--teal);
    transform-origin: left;
  }
  .contact {
    position: absolute;
    left: 40px; top: 120px;
  }
  .person-name {
    font-weight: 900;
    font-size: 34px;
    color: var(--ink);
    text-transform: uppercase;
    letter-spacing: .5px;
    padding-bottom: 8px;
    border-bottom: 1.5px solid var(--teal);
    display: inline-block;
  }
  .contact-list { list-style: none; margin-top: 8px; }
  .contact-item {
    display: flex; align-items: center; gap: 10px;
    color: var(--muted);
    font-size: 19px;
    line-height: 1.35;
  }
  .contact-item.phone { font-weight: 900; font-size: 21px; color: var(--ink); }
  .contact-item svg { width: 15px; height: 15px; flex: none; }
  .service-band {
    position: absolute;
    left: 0; right: 0; bottom: 0;
    height: 52px;
    background: var(--teal);
    display: flex; align-items: center;
    padding-left: 90px;
    clip-path: polygon(0 0, 100% 0, 100% 100%, 0 100%);
  }
  .service-band::after {
    content: "";
    position: absolute;
    right: 0; top: 0;
    width: 42px; height: 100%;
    background: var(--ink);
    clip-path: polygon(12px 0, 100% 0, 100% 100%, 0 100%);
  }
  .service-list {
    color: var(--ink);
    font-weight: 900;
    font-size: 15.5px;
    letter-spacing: .6px;
    text-transform: uppercase;
  }
</style>
</head>
<body>
  <section class="card card-front" aria-label="Business card front">
    <p class="brand-front">Birchline<br>Septic Solutions</p>
  </section>

  <section class="card card-back" aria-label="Business card back">
    <div class="pipe-pattern" role="img" aria-label="Faint background pattern of plumbing pipes and valves"></div>
    <p class="brand-back">Birchline Septic Solutions</p>
    <div class="divider-long"></div>
    <div class="contact">
      <h1 class="person-name">Tom Halvick</h1>
      <ul class="contact-list">
        <li class="contact-item phone">
          <svg viewBox="0 0 24 24" aria-hidden="true"><path fill="#0d0d0d" d="M6.6 10.8a15.1 15.1 0 0 0 6.6 6.6l2.2-2.2a1 1 0 0 1 1-.25 11.4 11.4 0 0 0 3.6.57 1 1 0 0 1 1 1V20a1 1 0 0 1-1 1A17 17 0 0 1 3 4a1 1 0 0 1 1-1h3.5a1 1 0 0 1 1 1c0 1.25.2 2.45.57 3.6a1 1 0 0 1-.25 1z"/></svg>
          555-241-0387
        </li>
        <li class="contact-item location">
          <svg viewBox="0 0 24 24" aria-hidden="true"><path fill="#0d0d0d" d="M12 2a7 7 0 0 0-7 7c0 5.2 7 13 7 13s7-7.8 7-13a7 7 0 0 0-7-7zm0 9.5A2.5 2.5 0 1 1 12 6.5a2.5 2.5 0 0 1 0 5z"/></svg>
          Maple Ridge, OH
        </li>
      </ul>
    </div>
    <div class="service-band">
      <p class="service-list">Pumping, Inspections, Installs &amp; Repairs</p>
    </div>
  </section>
</body>
</html>
```